Lawn care and snow removal company

Looking for a professional looking business card for a lawn care and snow removal company. Offering services to residential and small commercial properties. I have included a file of my logo. Please let me know if I can get you more information. Would like to print this with raised print. might help with the design. I have other logo files please tell me which file types you need more than happy to help.

Target Market(s)

Home owners, business owners, facilities superintendents, management staff.

Industry/Entity Type

Business

Requirements
Must have
• logo, space for website address
• Name
• Title , email and phone.
• I would also like to add serving the Millbrook Ashford Falls and surrounding communities to the card
Should not have
• Looking for professional, not cartoonish or silly.

```html
<!DOCTYPE html>
<html lang="en">
<head>
<meta charset="utf-8">
<title>Greenfrost Lawn &amp; Snow – Business Card</title>
<link rel="stylesheet" href="https://fonts.googleapis.com/css2?family=Open+Sans:wght@400;600;700&display=swap">
<style>
  :root {
    --brand-blue: #27a9e1;
    --brand-green: #8cc63f;
    --neutral-grey: #8a8a8a;
    --divider-grey: #8f8f8f;
    --paper: #ffffff;
    --wash-blue: #dce9f7;
    --wash-green: #e7f0d8;
  }
  * { margin: 0; padding: 0; box-sizing: border-box; }
  html, body {
    width: 1200px;
    height: 776px;
    overflow: hidden;
    background: var(--paper);
  }
  .business-card {
    position: relative;
    width: 1200px;
    height: 776px;
    background: var(--paper);
    font-family: "Open Sans", Arial, sans-serif;
    overflow: hidden;
  }
  .backdrop-wash { position: absolute; }
  .backdrop-wash--cool {
    left: 820px;
    top: 70px;
    width: 310px;
    height: 610px;
    background: radial-gradient(ellipse at 60% 50%, var(--wash-blue) 0%, rgba(220,233,247,0.55) 55%, rgba(255,255,255,0) 78%);
  }
  .backdrop-wash--fresh {
    left: 70px;
    top: 70px;
    width: 300px;
    height: 580px;
    background: linear-gradient(180deg, rgba(231,240,216,0) 0%, var(--wash-green) 45%, rgba(231,240,216,0.7) 100%);
    opacity: 0.75;
  }
  .brand-lockup {
    position: absolute;
    left: 128px;
    top: 160px;
    display: flex;
    align-items: center;
    gap: 22px;
  }
  .brand-lockup__mark {
    width: 22px;
    height: 22px;
    background: var(--brand-blue);
  }
  .brand-lockup__name {
    color: var(--brand-green);
    font-weight: 700;
    font-size: 52px;
    line-height: 62px;
    letter-spacing: 1px;
  }
  .identity {
    position: absolute;
    right: 132px;
    top: 334px;
    text-align: right;
  }
  .identity__name {
    color: var(--brand-blue);
    font-weight: 700;
    font-size: 54px;
    line-height: 66px;
    letter-spacing: 0.5px;
  }
  .identity__title {
    color: var(--brand-green);
    font-weight: 600;
    font-size: 28px;
    line-height: 34px;
  }
  .edge-tab {
    position: absolute;
    left: 1098px;
    top: 360px;
    width: 102px;
    height: 66px;
    background: var(--neutral-grey);
  }
  .divider {
    position: absolute;
    left: 130px;
    top: 443px;
    width: 940px;
    height: 2px;
    background: var(--divider-grey);
  }
  .contact-list {
    position: absolute;
    left: 130px;
    top: 478px;
    list-style: none;
    color: var(--brand-blue);
    font-weight: 700;
    font-size: 30px;
    line-height: 38px;
  }
  .contact-list__item {
    display: flex;
    align-items: center;
    gap: 18px;
  }
  .contact-list__icon {
    width: 24px;
    height: 24px;
    flex: none;
  }
  .service-area {
    position: absolute;
    left: 130px;
    top: 591px;
    color: var(--brand-blue);
    font-weight: 600;
    font-size: 30px;
    line-height: 38px;
    white-space: nowrap;
  }
  .footer-bands {
    position: absolute;
    left: 0;
    top: 0;
  }
</style>
</head>
<body>
  <main class="business-card">
    <div class="backdrop-wash backdrop-wash--fresh" role="img" aria-label="Soft green seasonal background accent"></div>
    <div class="backdrop-wash backdrop-wash--cool" role="img" aria-label="Soft blue seasonal background accent"></div>

    <div class="brand-lockup">
      <span class="brand-lockup__mark"></span>
      <div class="brand-lockup__name">GREENFROST<br>LAWN &amp; SNOW</div>
    </div>

    <div class="identity">
      <h1 class="identity__name">DANA HOLLOWAY</h1>
      <p class="identity__title">Owner</p>
    </div>

    <div class="edge-tab"></div>
    <div class="divider"></div>

    <ul class="contact-list">
      <li class="contact-list__item">
        <svg class="contact-list__icon" viewBox="0 0 24 24" aria-hidden="true">
          <path d="M7 2.5 L9.5 7 L7.8 9 C8.8 11.6 10.6 13.8 13.2 15.4 L15.3 13.8 L19.5 16.5 L18.2 20.5 C11 20 4.5 13 4 5.5 Z" fill="none" stroke="#8a8a8a" stroke-width="1.8" stroke-linejoin="round"/>
        </svg>
        <span>319-555-0148</span>
      </li>
      <li class="contact-list__item">
        <svg class="contact-list__icon" viewBox="0 0 24 24" aria-hidden="true">
          <g fill="none" stroke="#8a8a8a" stroke-width="1.5">
            <circle cx="12" cy="12" r="10"/>
            <ellipse cx="12" cy="12" rx="4.5" ry="10"/>
            <line x1="2" y1="12" x2="22" y2="12"/>
            <line x1="3.5" y1="7" x2="20.5" y2="7"/>
            <line x1="3.5" y1="17" x2="20.5" y2="17"/>
          </g>
        </svg>
        <span>www.greenfrostyard.com</span>
      </li>
      <li class="contact-list__item">
        <svg class="contact-list__icon" viewBox="0 0 24 24" aria-hidden="true">
          <g fill="none" stroke="#8a8a8a" stroke-width="1.8" stroke-linejoin="round">
            <rect x="2" y="5" width="20" height="14"/>
            <polyline points="2,5 12,13 22,5"/>
          </g>
        </svg>
        <span>DanaH@greenfrostyard.com</span>
      </li>
    </ul>

    <p class="service-area">Serving Millbrook Ashford Falls and Surrounding Communities</p>

    <svg class="footer-bands" width="1200" height="776" viewBox="0 0 1200 776" aria-hidden="true">
      <polygon points="0,650 569,650 659,776 0,776" fill="var(--brand-blue)"/>
      <polygon points="598,678 1200,678 1200,776 665,776" fill="var(--brand-green)"/>
    </svg>
  </main>
</body>
</html>
```